Wine Label: Tressivo

The project is to create 3 wine labels. The brand name is "Tressivo"

What we need is to have 3 versions: red wine, white wine and rose.

The wine is for young and modern people, between 21 and 31 years old, so it need to be casual, modern and fun, but at the same time it needs to keep the Premiums of a good European wine.

It is from Italy.

Target Market(s)

Young adults, between 21 and 31 years old. wine lovers

Requirements
Must have
• - Modern colors (Black, silver, red, etc.)
• - Clean label
• - Clear font
• - Style
• - The brand + the type of wine (red, white or rose)
Nice to have
• - A symbol to represent the brand
Should not have
• - Many elements
• - No clear fonts
• - No funny colors

```html
<!DOCTYPE html>
<html lang="en">
<head>
<meta charset="utf-8">
<title>Tressivo Wine Labels</title>
<link rel="stylesheet" href="https://fonts.googleapis.com/css2?family=Cormorant+Garamond:wght@300;400&family=Montserrat:wght@400;500&display=swap">
<style>
  :root {
    --canvas: #ffffff;
    --label-light: #f6f6f4;
    --label-red: #c0141b;
    --white-accent: #c9cf4a;
    --white-accent-soft: #e4e79a;
    --rose-accent: #e23a55;
    --rose-splash: #d45aa3;
    --rose-splash-soft: #f0a2c8;
    --red-splash: #f2b3cf;
    --red-splash-soft: #fbe1ec;
    --ink-grey: #8a8a85;
    --ink-light: #ffffff;
  }
  * { box-sizing: border-box; margin: 0; padding: 0; }
  html, body {
    width: 1200px; height: 1148px; overflow: hidden;
    background: var(--canvas);
  }
  .label-row {
    position: absolute; left: 50px; top: 364px;
    width: 1100px; height: 420px;
    display: flex; gap: 40px;
  }
  .wine-label {
    position: relative; width: 340px; height: 420px;
    background: var(--label-light);
    box-shadow: 0 1px 4px rgba(0,0,0,0.12);
    text-align: center;
    overflow: hidden;
  }
  .wine-label--red { background: var(--label-red); }
  .brand-name {
    margin-top: 36px;
    font-family: "Cormorant Garamond", serif;
    font-weight: 300; font-size: 46px;
    letter-spacing: 0.14em; text-indent: 0.14em;
    line-height: 1;
  }
  .wine-type {
    margin-top: 8px;
    font-family: "Montserrat", sans-serif;
    font-weight: 400; font-size: 14px;
    letter-spacing: 0.3em; text-indent: 0.3em;
  }
  .splash {
    position: absolute; left: 40px; top: 110px;
    width: 270px; height: 200px;
  }
  .winery-name {
    position: absolute; left: 0; right: 0; top: 308px;
    font-family: "Montserrat", sans-serif;
    font-size: 13px; letter-spacing: 0.2em;
  }
  .label-footer {
    position: absolute; left: 22px; right: 22px; bottom: 26px;
    display: flex; justify-content: space-between; align-items: flex-end;
    font-family: "Montserrat", sans-serif;
    font-size: 7px; letter-spacing: 0.1em; line-height: 1.5;
  }
  .tagline { text-align: center; }

  .wine-label--white .brand-name,
  .wine-label--white .wine-type { color: var(--white-accent); }
  .wine-label--white .winery-name { color: var(--white-accent); }
  .wine-label--rose .brand-name { color: var(--rose-accent); }
  .wine-label--rose .wine-type,
  .wine-label--rose .winery-name { color: var(--rose-splash); }
  .wine-label--white .label-footer,
  .wine-label--rose .label-footer { color: var(--ink-grey); }
  .wine-label--red .brand-name,
  .wine-label--red .wine-type,
  .wine-label--red .winery-name,
  .wine-label--red .label-footer { color: var(--ink-light); }
</style>
</head>
<body>
<main class="label-row">

  <section class="wine-label wine-label--white">
    <h1 class="brand-name">TRESSIVO</h1>
    <p class="wine-type">WHITE</p>
    <svg class="splash" viewBox="0 0 270 200" role="img" aria-label="Watercolour splash of raised hands in pale yellow-green">
      <defs>
        <radialGradient id="splash-white" cx="45%" cy="60%" r="60%">
          <stop offset="0" stop-color="var(--white-accent)"/>
          <stop offset="1" stop-color="var(--white-accent-soft)" stop-opacity="0.5"/>
        </radialGradient>
      </defs>
      <path d="M20 150 C40 110 70 90 90 60 C110 30 150 20 175 40 C200 60 240 70 250 110 C258 150 220 185 170 190 C120 195 60 190 20 150 Z" fill="url(#splash-white)"/>
    </svg>
    <p class="winery-name">WINERY NAME</p>
    <div class="label-footer">
      <span>750 ml</span>
      <span class="tagline">SOMETHING CLEVER<br>WINE of ITALY</span>
      <span>13% vol</span>
    </div>
  </section>

  <section class="wine-label wine-label--rose">
    <h1 class="brand-name">TRESSIVO</h1>
    <p class="wine-type">ROSE</p>
    <svg class="splash" viewBox="0 0 270 200" role="img" aria-label="Watercolour splash of raised hands in pink and magenta">
      <defs>
        <radialGradient id="splash-rose" cx="40%" cy="55%" r="60%">
          <stop offset="0" stop-color="var(--rose-accent)"/>
          <stop offset="0.5" stop-color="var(--rose-splash)"/>
          <stop offset="1" stop-color="var(--rose-splash-soft)" stop-opacity="0.5"/>
        </radialGradient>
      </defs>
      <path d="M20 150 C40 110 70 90 90 60 C110 30 150 20 175 40 C200 60 240 70 250 110 C258 150 220 185 170 190 C120 195 60 190 20 150 Z" fill="url(#splash-rose)"/>
    </svg>
    <p class="winery-name">WINERY NAME</p>
    <div class="label-footer">
      <span>750 ml</span>
      <span class="tagline">SOMETHING CLEVER<br>WINE of ITALY</span>
      <span>13% vol</span>
    </div>
  </section>

  <section class="wine-label wine-label--red">
    <h1 class="brand-name">TRESSIVO</h1>
    <p class="wine-type">RED</p>
    <svg class="splash" viewBox="0 0 270 200" role="img" aria-label="Watercolour splash of raised hands in soft pink">
      <defs>
        <radialGradient id="splash-red" cx="40%" cy="55%" r="60%">
          <stop offset="0" stop-color="var(--red-splash)"/>
          <stop offset="1" stop-color="var(--red-splash-soft)" stop-opacity="0.6"/>
        </radialGradient>
      </defs>
      <path d="M20 150 C40 110 70 90 90 60 C110 30 150 20 175 40 C200 60 240 70 250 110 C258 150 220 185 170 190 C120 195 60 190 20 150 Z" fill="url(#splash-red)"/>
    </svg>
    <p class="winery-name">WINERY NAME</p>
    <div class="label-footer">
      <span>750 ml</span>
      <span class="tagline">SOMETHING CLEVER<br>WINE of ITALY</span>
      <span>13% vol</span>
    </div>
  </section>

</main>
</body>
</html>
```